Re-Design Of High Traffic Content Hub

“Roadbound Haven, is a comprehensive online hub dedicated to helping over 150,000 visitors a month have a smooth towing trip. Roadbound Haven is the place where you’ll find up-to-date information, practical advice, ‘how to’ guides and handy tips for your caravan, trailer and anything else you need to tow."

Content on the site is split in to 4 main pillars:
“Caravan” “Trailer” “Boating” "Travel"

Each pillar is split further in to 3 categories:
How To • Products • Reviews

We are crowd-sourcing the redesign of the following pages:

- Home Page
- Category Page
- Single Post
- Search Results
- Static Content Page (Terms & Conditions/ About / Privacy Policy)

Look and feel to be implemented inline with UX best practice.
A strong conversion focus is desirable site wide (e-book downloads & newsletter subscriptions are offered).

Our preference is for the home page to provide the visitor with a visual snapshot of fresh site content and encourage the user to explore the site further using navigation or search.

Design elements to be featured on the home page:
Main Navigation
Site Search
Newsletter Subscription Box
eBook Download CTA
Mission Statement
2 x Recent articles from each top level content pillar including featured image and title.
An area to feature 3 of the site's best performing articles including featured image, title and excerpt.

Mission Statement: "Roadbound Haven is the place you can turn to for up-to-date information, practical advice, ‘how to’ guides and handy tips for your caravan, trailer and anything else worth towing. "

Selected designs will be coded in responsive bootstrap so preference will be given to designs presented with this in mind.

Logo's attached in transparent white and transparent dark.

Live site located at www.roadboundhaven.com.au

• Strong conversion focus (eBook downloads and newsletter subscriptions)

```html
<!DOCTYPE html>
<html lang="en">
<head>
<meta charset="utf-8">
<title>Roadbound Haven</title>
<link href="https://fonts.googleapis.com/css2?family=Oswald:wght@300;400;500&display=swap" rel="stylesheet">
<style>
:root{
  --red:#e3001b;
  --ink:#2b2b2b;
  --muted:#8a8a8a;
  --line:#b9b9b9;
  --paper:#ffffff;
  --mist:#f4f4f4;
}
*{box-sizing:border-box;margin:0;padding:0}
html,body{width:710px;height:1200px;overflow:hidden}
body{position:relative;background:var(--paper);font-family:'Oswald',sans-serif;font-weight:300;color:var(--ink)}
.hero{position:absolute;left:0;top:0;width:710px;height:350px;
  background:linear-gradient(180deg,#3f5a52 0%,#6f7d5c 35%,#4b4a33 60%,#3a3325 100%);
  clip-path:polygon(0 0,710px 0,710px 225px,0 350px)}
.brand{position:absolute;left:86px;top:12px;display:flex;align-items:flex-start;gap:6px}
.brand-name{color:#fff;font-weight:500;font-size:12px;line-height:12px;text-transform:uppercase;width:58px}
.brand-mark{width:24px;height:36px;background:var(--red)}
.nav{position:absolute;left:437px;top:27px;display:flex;gap:15px;align-items:center}
.nav a{color:#fff;text-decoration:none;font-size:8px;font-weight:300}
.hero-title{position:absolute;left:84px;top:93px;color:#fff;font-weight:400;font-size:19px;letter-spacing:-.2px}
.hero-text{position:absolute;left:84px;top:119px;width:236px;color:#fff;font-size:10.5px;line-height:15px}
.field{position:absolute;height:22px;border:1.5px solid #fff;border-radius:11px;color:#fff;font-size:9px;padding:4px 10px}
.hero-email{left:84px;top:200px;width:166px}
.hero-btn{left:258px;top:200px;width:77px;background:#fff;color:#444;text-align:center;font-size:8.5px}
.caravan{position:absolute;left:354px;top:158px;width:302px;height:182px;border-radius:30px 14px 8px 50px;
  background:linear-gradient(180deg,#f2f2f2 0%,#dcdcdc 60%,#5b5e63 100%)}
.mission{position:absolute;top:410px;width:710px;text-align:center;font-size:15px;font-weight:300}
.pillar{position:absolute;top:478px;width:170px}
.pillar-icon{position:absolute;left:0;top:2px;width:32px;height:32px;border-radius:50%;border:1px solid #e6e6e6;display:flex;align-items:center;justify-content:center}
.pillar h3{margin-left:43px;font-weight:300;font-size:10.5px}
.pillar p{margin-left:43px;margin-top:5px;font-size:7px;line-height:9px;color:var(--muted)}
.news{position:absolute;left:0;top:573px;width:710px;height:405px;background:var(--mist)}
.news-title{position:absolute;top:46px;width:710px;text-align:center;font-weight:400;font-size:15px}
.card{position:absolute;top:111px;width:169px}
.card-img{height:90px}
.card-head{position:relative;margin-top:10px;height:33px;border-bottom:1px solid var(--line)}
.date{position:absolute;left:0;top:0;width:24px;height:33px;background:var(--red);color:#fff;text-align:center;font-size:12px;line-height:14px;padding-top:2px}
.date small{display:block;font-size:5px;line-height:6px}
.card-head h4{margin-left:38px;width:112px;font-weight:300;font-size:11px;line-height:13px;color:#555}
.card p{margin-top:9px;font-size:7px;line-height:11px;color:var(--muted)}
.meta{margin-top:8px;font-size:5.5px;color:var(--muted);display:flex;gap:10px}
.all-news{position:absolute;left:294px;top:344px;width:115px;height:22px;border:1px solid #333;border-radius:11px;text-align:center;font-size:8px;line-height:20px;font-weight:400}
.newsletter{position:absolute;left:0;top:978px;width:710px;height:186px;background:linear-gradient(180deg,#2a2c2e 0%,#3b3a36 55%,#1a1b1d 100%)}
.newsletter h2{position:absolute;top:54px;width:710px;text-align:center;color:#fff;font-weight:400;font-size:20px}
.newsletter p{position:absolute;left:188px;top:86px;width:340px;text-align:center;color:#fff;font-size:7px;line-height:9.5px}
.nl-email{left:208px;top:118px;width:292px;height:24px;color:#fff}
.nl-btn{position:absolute;left:428px;top:120px;width:70px;height:20px;background:var(--red);border-radius:10px;color:#fff;font-size:8px;font-weight:400;text-align:center;line-height:20px}
.footer{position:absolute;left:0;top:1164px;width:710px;height:36px}
.footer-note{position:absolute;left:86px;top:13px;font-size:6.5px;color:var(--muted)}
.footer-note b{color:var(--red);font-weight:300}
.social{position:absolute;left:558px;top:12px;display:flex;gap:21px}
.social span{width:9px;height:9px;border-radius:50%;background:#333}
</style>
</head>
<body>
<header class="hero" role="img" aria-label="Photo of a long straight road through hills under a cloudy sky"></header>
<div class="brand"><span class="brand-name">Roadbound Haven</span><span class="brand-mark"></span></div>
<nav class="nav">
  <a href="#">HOME</a><a href="#">CARAVAN</a><a href="#">TRAILERS</a><a href="#">BOATS</a><a href="#">TRAVEL</a>
  <svg width="10" height="10" viewBox="0 0 10 10" fill="none" stroke="#fff" stroke-width="1.1"><circle cx="4.2" cy="4.2" r="3.4"/><path d="M6.8 6.8 9.5 9.5"/></svg>
</nav>
<h1 class="hero-title">DOWNLOAD OUR FREE E-BOOK</h1>
<p class="hero-text">Our towing e-book, packed full of essential safety, preparation and towing tips will be the perfect driving companion. Receive your free e-book and sign up to our newsletter now!</p>
<div class="field hero-email">Email</div>
<div class="field hero-btn">DOWNLOAD</div>
<div class="caravan" role="img" aria-label="Photo of a white pop-top caravan on a twin-axle trailer"></div>

<p class="mission">Roadbound Haven is the place you can turn to for up-to- date information</p>

<div class="pillar" style="left:78px">
  <span class="pillar-icon"><svg width="18" height="14" viewBox="0 0 18 14" fill="none" stroke="#e3001b" stroke-width="1.2"><rect x="1" y="2" width="14" height="8" rx="2"/><circle cx="6" cy="11" r="1.6"/><path d="M15 9h2M3 5h4v3H3z"/></svg></span>
  <h3>CARAVANING</h3>
  <p>Here, we nominate our top three must-do NSW caravanning destinations.</p>
</div>
<div class="pillar" style="left:267px">
  <span class="pillar-icon"><svg width="18" height="14" viewBox="0 0 18 14" fill="none" stroke="#e3001b" stroke-width="1.2"><path d="M2 3h10v7H2zM12 5h3l2 3v2h-5"/><circle cx="5" cy="11" r="1.6"/><circle cx="14" cy="11" r="1.6"/></svg></span>
  <h3>TRAILERS</h3>
  <p>The jockey wheel is one of the most vital parts of any caravan but they do eventually require some maintenance.</p>
</div>
<div class="pillar" style="left:454px">
  <span class="pillar-icon"><svg width="20" height="14" viewBox="0 0 20 14" fill="none" stroke="#e3001b" stroke-width="1.2"><path d="M1 9h18l-3 4H4zM5 9l2-4h6l3 4M1 13c3-1 5 1 9 0s6 1 9 0"/></svg></span>
  <h3>BOATING</h3>
  <p>Where will you take your trailer boat for your next holiday? We've found some of the best destinations around Australia.</p>
</div>

<section class="news">
  <h2 class="news-title">Latest News</h2>
  <article class="card" style="left:89px">
    <div class="card-img" role="img" aria-label="Hand holding a phone showing a tracking app over a road map" style="background:linear-gradient(90deg,#d9dccf 0%,#eae6d6 55%,#9cc9e8 100%)"></div>
    <div class="card-head"><span class="date">03<small>JUN</small></span><h4>How To Theft-Proof Your Caravan</h4></div>
    <p>Want to ensure your caravan is virtually theft-proof? The Axelon Guardlock 3 is the answer.</p>
    <div class="meta"><span>John Doe</span><span>80</span><span>456</span></div>
  </article>
  <article class="card" style="left:271px">
    <div class="card-img" role="img" aria-label="Close-up of a coil spring caravan suspension" style="background:linear-gradient(90deg,#6d6f72 0%,#b9bbbd 50%,#8c8e90 100%)"></div>
    <div class="card-head"><span class="date">03<small>JUN</small></span><h4>New Caravan Suspension Launched</h4></div>
    <p>Axelon's TrailFlex caravan suspension is set to change the way we travel.</p>
    <div class="meta"><span>John Doe</span><span>80</span><span>456</span></div>
  </article>
  <article class="card" style="left:454px">
    <div class="card-img" role="img" aria-label="Red portable generator on a campsite at dusk" style="background:linear-gradient(180deg,#8a5a3a 0%,#5a4232 50%,#3b2e26 100%)"></div>
    <div class="card-head"><span class="date">03<small>JUN</small></span><h4>How To Use A Generator</h4></div>
    <p>Do you power your caravan or motorhome with a generator? If so, here are some basic courtesies.</p>
    <div class="meta"><span>John Doe</span><span>80</span><span>456</span></div>
  </article>
  <div class="all-news">ALL NEWS</div>
</section>

<section class="newsletter" role="img" aria-label="Night photo of a winding coastal road and bay">
  <h2>FREE WEEKLY NEWSLETTERS</h2>
  <p>Roadbound Haven is the place you can turn to for up-to-date information, practical advice, ‘how to’ guides and handy tips for your caravan, trailer and anything else worth towing. To receive regular towing hints, tips sign up to our newsletter today!</p>
  <div class="field nl-email">Your e-mail</div>
  <div class="nl-btn">Subscribe</div>
</section>

<footer class="footer">
  <p class="footer-note">©2016 - <b>ROADBOUND HAVEN.</b></p>
  <div class="social"><span></span><span></span><span></span></div>
</footer>
</body>
</html>
```